nutrition ebook cover

i need a cover for a ebook designed, the book is called Amber Lattice so i would like that somewhere on the cover. i would also like the word nutrition followed by my company logo that i have attached below somewhere on the cover( i have attached two logos and would like to see with both separatley), i would like this to be faded into the background if possible, perhaps in a upper or lower corner. i would also like to see options with and without the picture i have attached below. the look I'm going for is professional and clean. this is a fat loss, healthy eating booklet. the winning designer i would like to design the following pages within the book aswell no more than 10 pages, that i will provide all content for, i just need help with putting what i have on pdf in a way that looks professional and cool. this would ideally covered in the rate that is paid for the cover. i also have other booklets i need made so the winning designer will most likely get that work too at a later date for an additional fee of course.

Industry/Entity Type

Nutrition

Requirements
Nice to have
• Outside images are welcomed, happy to purchase any stock images used from a outside source

```html
<!DOCTYPE html>
<html lang="en">
<head>
<meta charset="utf-8">
<title>Amber Lattice — ebook cover options</title>
<link rel="stylesheet" href="https://fonts.googleapis.com/css2?family=Alfa+Slab+One&family=Cinzel:wght@700&family=Nunito:wght@600&display=swap">
<style>
  :root {
    --page: #ffffff;
    --slate-deep: #1c2a2c;
    --slate: #2e4347;
    --wood-light: #d9a07a;
    --wood: #b9714a;
    --wood-dark: #7d4328;
    --greens: #3f6b34;
    --title-red: #7e1e14;
    --title-red-deep: #5e1610;
    --brand-text: #eef3f1;
  }
  * { box-sizing: border-box; margin: 0; padding: 0; }
  html, body {
    width: 1200px; height: 890px; overflow: hidden;
    background: var(--page);
  }
  .canvas {
    position: relative; width: 1200px; height: 890px;
  }
  .cover {
    position: absolute; top: 32px; width: 537px; height: 806px;
    overflow: hidden; background: var(--slate-deep);
  }
  .cover--wordmark { left: 38px; }
  .cover--badge { left: 612px; }

  .cover__photo {
    position: absolute; inset: 0;
    background:
      radial-gradient(ellipse 48% 40% at 52% 50%, var(--wood-light) 0%, var(--wood) 55%, var(--wood-dark) 75%, transparent 90%),
      radial-gradient(ellipse 60% 22% at 45% 12%, var(--greens) 0%, transparent 70%),
      radial-gradient(ellipse 80% 30% at 60% 92%, var(--greens) 0%, transparent 70%),
      linear-gradient(160deg, var(--slate) 0%, var(--slate-deep) 100%);
  }
  .cover__fade {
    position: absolute; left: 0; right: 0; bottom: 0; height: 140px;
    background: linear-gradient(to bottom, rgba(28,42,44,0) 0%, rgba(28,42,44,0.92) 45%, var(--slate-deep) 100%);
  }

  .title {
    position: absolute; left: 0; right: 0; top: 262px;
    text-align: center;
  }
  .title__main {
    display: block;
    font-family: "Alfa Slab One", serif;
    font-size: 112px; line-height: 1.9;
    line-height: 200px;
    color: var(--title-red);
    letter-spacing: -1px;
    text-shadow: 0 0 2px rgba(240,190,150,0.7);
  }
  .title__sub {
    display: block;
    font-family: "Cinzel", serif;
    font-weight: 700;
    font-size: 56px; line-height: 56px;
    color: var(--title-red-deep);
    letter-spacing: 1px;
    margin-top: 6px;
  }

  .brand {
    position: absolute; right: 30px; bottom: 22px;
    display: flex; align-items: center; gap: 8px;
    font-family: "Nunito", sans-serif; font-weight: 600;
    color: var(--brand-text);
  }
  .brand__name { font-size: 31px; line-height: 1; }
  .cover--badge .brand { right: 22px; bottom: 14px; }
  .cover--badge .brand__name { font-size: 25px; }
  .brand__seal {
    width: 84px; height: 84px; border-radius: 50%;
    border: 2px solid var(--brand-text);
  }
</style>
</head>
<body>
<main class="canvas">

  <section class="cover cover--wordmark">
    <div class="cover__photo" role="img" aria-label="Overhead photo of a wooden cutting board on a dark slate table surrounded by broccoli, tomatoes, mushrooms, lemon, rocket, onion and a potato"></div>
    <div class="cover__fade"></div>
    <h1 class="title">
      <span class="title__main">Amber</span>
      <span class="title__sub">LATTICE</span>
    </h1>
    <div class="brand">
      <span class="brand__name">Nutrition Kestrel</span>
    </div>
  </section>

  <section class="cover cover--badge">
    <div class="cover__photo" role="img" aria-label="Overhead photo of a wooden cutting board on a dark slate table surrounded by broccoli, tomatoes, mushrooms, lemon, rocket, onion and a potato"></div>
    <div class="cover__fade"></div>
    <h1 class="title">
      <span class="title__main">Amber</span>
      <span class="title__sub">LATTICE</span>
    </h1>
    <div class="brand">
      <span class="brand__name">Nutrition Kestrel</span>
      <span class="brand__seal" aria-hidden="true"></span>
    </div>
  </section>

</main>
</body>
</html>
```